web site to find a reliable, local tradesman, handyman or builder for any job

Design a web site as marketplace for handyman and client.
Handyman can
* set their profile (name, address, contacts)
* search / view / apply for job offers (by setting a new offer)
Client can
* search / view job offers
* generate new job offers (title, description, max price, date, duration, location).
* select and rate a job
Main functions would be SEARCH / VIEW to see in one glance WHAT needs to be done WHERE. The contractors then exchange contacts.
Handyman

```html
<!DOCTYPE html>
<html lang="en">
<head>
<meta charset="utf-8">
<title>tradefinder – find a local handyman</title>
<link rel="stylesheet" href="https://fonts.googleapis.com/css2?family=Arimo:ital,wght@0,400;0,700;1,400;1,700&display=swap">
<style>
:root{
  --page:#ebebeb;
  --panel:#ffffff;
  --ink:#333333;
  --ink-soft:#444444;
  --brand:#5b9a2e;
  --green:#80c41c;
  --green-dark:#5f9312;
  --blue:#3c74b8;
  --blue-light:#6a9fdc;
  --link:#1f5ea8;
  --nav-top:#2e2e2e;
  --nav-bottom:#121212;
  --btn:#222222;
  --beige-light:#ece2d7;
  --beige-dark:#c7ae95;
  --beige-ink:#9a7b5e;
  --band:#f1f1f1;
  --badge:#9a9a9a;
}
*{box-sizing:border-box;margin:0;padding:0}
html,body{width:910px;height:1200px;overflow:hidden}
body{background:var(--page);font-family:"Arimo",Arial,sans-serif;color:var(--ink);position:relative}
.abs{position:absolute}

/* header */
.brand-name{left:53px;top:18px;font-weight:700;font-size:34px;line-height:32px;color:var(--brand);letter-spacing:-0.5px}
.brand-name span{display:block}
.brand-name span+span{padding-left:12px}
.phone{right:55px;top:28px;font-weight:700;font-size:15px;color:#444;letter-spacing:.5px}
.search{left:642px;top:57px;width:213px;height:28px;border-radius:4px;background:linear-gradient(#8a8a8a,#5d5d5d);box-shadow:inset 0 1px 2px rgba(0,0,0,.4)}
.search span{position:absolute;left:15px;top:8px;font-size:10px;font-style:italic;color:#eee}
.search svg{position:absolute;right:8px;top:5px}

/* navigation */
.nav{left:53px;top:106px;width:803px;height:58px;border-radius:4px;background:linear-gradient(var(--nav-top),var(--nav-bottom));box-shadow:0 2px 4px rgba(0,0,0,.3);display:flex;overflow:hidden}
.nav a{display:flex;align-items:center;justify-content:center;color:#f2f2f2;font-size:12.5px;text-decoration:none;border-right:1px solid #3c3c3c;height:100%;letter-spacing:.2px}
.nav a.active{background:#050505}
.nav .caret{margin-left:7px;width:0;height:0;border-left:5px solid transparent;border-right:5px solid transparent;border-top:5px solid #ddd}

/* main panel */
.main{left:53px;top:178px;width:803px;height:948px;background:var(--panel);border:1px solid #d6d6d6;box-shadow:0 0 5px rgba(0,0,0,.18)}
.hero{left:63px;top:184px;width:784px;height:253px;border:1px solid #cfcfcf;overflow:hidden}
.hero-text{left:0;top:0;width:369px;height:253px;background:linear-gradient(90deg,var(--beige-light),var(--beige-dark))}
.hero-text h2{position:absolute;left:55px;top:54px;font-size:20px;font-weight:700;font-style:italic;color:var(--beige-ink);letter-spacing:.3px}
.hero-text p{position:absolute;left:30px;top:101px;width:330px;font-size:10px;line-height:16px;color:#333}
.btn-dark{background:var(--btn);color:#fff;font-size:9px;font-style:italic;display:flex;align-items:center;justify-content:center;border:1px solid #777}
.hero-text .btn-dark{position:absolute;left:289px;top:146px;width:55px;height:18px}
.dots{position:absolute;left:124px;top:215px;display:flex;gap:15px}
.dots i{width:11px;height:11px;border-radius:50%;background:#fff;display:block}
.dots i.on{background:#222}
.hero-photo{left:369px;top:0;width:415px;height:253px;background:linear-gradient(120deg,#e9e4dc,#b9a895 55%,#f2efea)}
.hero-shadow{left:90px;top:437px;width:730px;height:14px;background:radial-gradient(ellipse at top,rgba(0,0,0,.22),transparent 70%)}

/* green boxes */
.box{background:var(--green);border-radius:3px}
.tab{height:39px;border-radius:5px 5px 0 0;background:linear-gradient(var(--blue-light),var(--blue));border:1px solid #2d5d98;color:#fff;font-weight:700;font-style:italic;font-size:12.5px;display:flex;align-items:center}
.tab .icon{width:34px;height:30px;margin:0 14px 0 18px;border-radius:4px;background:linear-gradient(#f6d34a,#d9a412)}
.tab .icon.doc{width:22px;background:linear-gradient(90deg,#e7eef5,#8fa6bd);margin:0 20px 0 24px}
.login{left:62px;top:480px;width:255px;height:169px}
.login-tab{left:85px;top:460px;width:208px}
.field-label{color:#fff;font-size:10.5px;font-weight:700}
.field{width:161px;height:27px;border-radius:5px;background:linear-gradient(#f4f4f4,#fff);border:1px solid #c4c4c4}
.company-login{left:127px;top:612px;font-size:11.5px;font-weight:700;font-style:italic;text-decoration:underline;color:#222}
.login-btn{left:241px;top:606px;width:60px;height:22px;border-radius:4px;background:linear-gradient(#fff,#d6d6d6);border:1px solid #9fb57a;color:var(--green-dark);font-size:11px;font-weight:700;font-style:italic;display:flex;align-items:center;justify-content:center}
.offers{left:328px;top:480px;width:518px;height:169px}
.offers-tab{left:351px;top:460px;width:208px}
.offers-col{position:absolute;font-size:10.5px;font-style:italic;color:#222;line-height:17px}
.offers-col b{font-weight:700}
.offers-left{left:14px;top:33px;width:118px}
.offers-rule{position:absolute;left:142px;top:32px;width:1px;height:110px;background:var(--green-dark)}
.offers-right{left:161px;top:33px;width:352px}
.offers-right p{margin-bottom:6px}
.offers-right .hang{padding-left:66px;text-indent:-66px}

/* content */
.heading{font-size:12px;font-weight:700;font-style:italic;color:var(--ink);letter-spacing:.3px}
.copy{font-size:10px;line-height:16.5px;color:var(--ink-soft);text-align:justify;width:481px}
.more-link{font-size:11px;font-weight:700;font-style:italic;color:#333}
.tagline{left:560px;top:716px;width:275px;text-align:center;font-size:16px;font-weight:700;font-style:italic;color:var(--ink);line-height:22px}
.tagline em{color:var(--brand);font-size:17.5px}
.links{left:68px;top:930px;width:480px;display:grid;grid-template-columns:166px 180px 130px;row-gap:6px}
.links a{font-size:11px;font-style:italic;color:var(--link);text-decoration:underline;display:flex;align-items:center;height:15.5px}
.links a::before{content:"";width:0;height:0;border-top:4px solid transparent;border-bottom:4px solid transparent;border-left:5px solid var(--link);margin-right:10px}

.card{left:563px;width:272px;height:92px;border-radius:3px;background:linear-gradient(#ffffff,#dcdcdc);box-shadow:0 1px 2px rgba(0,0,0,.15)}
.card h3{position:absolute;left:72px;top:10px;font-size:12px;font-weight:700;font-style:italic;color:#333}
.card p{position:absolute;left:92px;top:31px;font-size:12px;font-weight:700;font-style:italic;color:var(--link)}
.card .btn-dark{position:absolute;left:175px;top:58px;width:57px;height:21px;border-radius:3px;font-weight:700}
.card .art{position:absolute;left:18px;top:28px;width:50px;height:52px;border-radius:6px}
.art-people{background:linear-gradient(#e7c9a6,#4c5866)}
.art-tool{background:linear-gradient(135deg,#b8b8b8,#e2b21b)}

.partners{left:54px;top:1040px;width:801px;height:85px;background:var(--band)}
.partners h4{position:absolute;left:34px;top:26px;width:120px;text-align:center;font-size:11.5px;font-weight:700;font-style:italic;color:#555;line-height:16px}
.badge{position:absolute;background:var(--badge);opacity:.55;border-radius:3px}

/* footer */
.copyright{left:62px;top:1154px;font-size:9.5px;color:#333}
.social{left:618px;top:1149px;display:flex;align-items:center;gap:9px;font-size:9.5px;color:#333}
.social span.label{margin-right:2px}
.social i{display:block;width:22px;height:22px;border-radius:3px}
</style>
</head>
<body>

<header>
  <div class="abs brand-name" aria-label="tradefinder"><span>trade</span><span>finder</span></div>
  <div class="abs phone">Call us : 555 010 2040</div>
  <div class="abs search">
    <span>Search...</span>
    <svg width="18" height="18" viewBox="0 0 18 18" aria-hidden="true"><circle cx="7" cy="7" r="5" fill="none" stroke="#fff" stroke-width="2.4"/><line x1="10.5" y1="10.5" x2="16" y2="16" stroke="#fff" stroke-width="3" stroke-linecap="round"/></svg>
  </div>
</header>

<nav class="abs nav">
  <a class="active" style="width:85px">HOME</a>
  <a style="width:101px">ABOUT US</a>
  <a style="width:103px">SERVICES</a>
  <a style="width:163px">HANDYMAN SEARCH</a>
  <a style="width:75px">JOBS<i class="caret"></i></a>
  <a style="width:120px">CONTACT US</a>
  <a style="width:105px;border-right:none">REGISTER</a>
</nav>

<main>
  <div class="abs main"></div>

  <section class="abs hero">
    <div class="abs hero-text">
      <h2>Lorem Ipusem Contantry</h2>
      <p>Marcus are also reproduced in their exact original form, accompanied by English versions from the 1914 translation by J. Morrow.</p>
      <a class="btn-dark">View more</a>
      <div class="dots"><i class="on"></i><i></i><i></i><i></i><i></i></div>
    </div>
    <div class="abs hero-photo" role="img" aria-label="Photo of a handyman with a clipboard discussing a bathroom job with a client"></div>
  </section>
  <div class="abs hero-shadow"></div>

  <section>
    <div class="abs box login"></div>
    <div class="abs tab login-tab"><i class="icon" role="img" aria-label="Yellow hard hat illustration"></i>Handy man’s Log in</div>
    <div class="abs field-label" style="left:77px;top:522px">username :</div>
    <div class="abs field" style="left:140px;top:516px"></div>
    <div class="abs field-label" style="left:77px;top:567px">Password :</div>
    <div class="abs field" style="left:140px;top:559px"></div>
    <div class="abs company-login">Company Log in</div>
    <div class="abs login-btn">Log in</div>
  </section>

  <section>
    <div class="abs box offers">
      <div class="offers-col offers-left">
        <p><b>Company Details</b></p>
        <p style="margin-top:5px">Exact original form, accompanied English versions<br>&nbsp;J. Morrow.<br>Call us : 555 010 7788</p>
      </div>
      <div class="offers-rule"></div>
      <div class="offers-col offers-right">
        <p><b>Job Title : Marcus are also reproduced</b></p>
        <p class="hang"><b>Description :</b> Exact original form, accompanied by English versions from the 1914 translation by J. Morrow.</p>
        <p><b>Description : $ 321</b> &nbsp;&nbsp;&nbsp;&nbsp;&nbsp;&nbsp;<b>Date : 10.11.2011</b> &nbsp;&nbsp;&nbsp;&nbsp;<b>Duration : 8 hours</b></p>
        <p><b>Location :</b> Exact original form, accompanied by English versions</p>
      </div>
    </div>
    <div class="abs tab offers-tab"><i class="icon doc" role="img" aria-label="Office document illustration"></i>Company Offers</div>
  </section>

  <section>
    <h2 class="abs heading" style="left:62px;top:666px">Welcome To Our Site</h2>
    <p class="abs copy" style="left:62px;top:684px">Many desktop publishing packages and web page editors now use Lorem Ipsum as their default model text, and a search for 'lorem ipsum' will uncover many web sites still in their infancy. Various versions have volved over the years, sometimes by accident, sometimes on purpose (injected humour and the like). The standard chunk of Lorem Ipsum used since the 1500s is reproduced below for those interested. Sections 1.10.32 and 1.10.33 from "de Finibus Bonorum et Malorum" by Marcus are also reproduced in their exact original form, accompanied by English versions from the 1914 translation by J. Morrow.</p>
    <a class="abs more-link" style="left:482px;top:795px">View more</a>

    <h2 class="abs heading" style="left:62px;top:829px">Our Services</h2>
    <p class="abs copy" style="left:62px;top:853px">Many desktop publishing packages and web page editors now use Lorem Ipsum as their default model text, and a search for 'lorem ipsum' will uncover many web sites still in their infancy. Various versions have volved over the years, sometimes by accident, sometimes on purpose (injected humour and the like). The standard chunk of Lorem Ipsum used since the 1500s is reproduced below for those interested.</p>
    <div class="abs links">
      <a>Lorem ipsum dolor</a><a>Lorem ipsum dolor</a><a>Lorem ipsum dolor</a>
      <a>consectetur adipiscing</a><a>consectetur adipiscing</a><a>consectetur adipiscing</a>
      <a>Phasellus id</a><a>Phasellus id</a><a>Phasellus id</a>
    </div>
  </section>

  <aside>
    <p class="abs tagline">Thousands of <em>Handymans</em> will<br>join with us</p>
    <div class="abs card" style="top:823px">
      <i class="art art-people" role="img" aria-label="Illustration of two tradesmen in hard hats"></i>
      <h3>Looking for a Handyman?</h3>
      <p>Hire them from here...</p>
      <a class="btn-dark">View more</a>
    </div>
    <div class="abs card" style="top:932px">
      <i class="art art-tool" role="img" aria-label="Illustration of a claw hammer"></i>
      <h3>Looking for a Good job?</h3>
      <p style="left:84px">Find a good job from here...</p>
      <a class="btn-dark">View more</a>
    </div>
  </aside>

  <section class="abs partners">
    <h4>Company who join<br>with us</h4>
    <i class="badge" style="left:211px;top:24px;width:56px;height:36px"></i>
    <i class="badge" style="left:318px;top:22px;width:36px;height:38px"></i>
    <i class="badge" style="left:414px;top:24px;width:90px;height:34px"></i>
    <i class="badge" style="left:551px;top:28px;width:103px;height:30px"></i>
    <i class="badge" style="left:700px;top:32px;width:91px;height:24px"></i>
  </section>
</main>

<footer>
  <div class="abs copyright">Copyright © 2011 www.tradefinder.example All rights reserved</div>
  <div class="abs social">
    <span class="label">Connect with us :</span>
    <i style="background:#3b5a9a" aria-label="Social network one"></i>
    <i style="background:#4db7e5" aria-label="Social network two"></i>
    <i style="background:#f26b21" aria-label="Social network three"></i>
    <i style="background:#1a75b0" aria-label="Social network four"></i>
    <i style="background:#4c9a48" aria-label="Social network five"></i>
  </div>
</footer>

</body>
</html>
```